Australian Skilled Migration

We need to design a add/flyer for a newspaper/magazine to promote our Australian Migration firm services. We targeting overseas graduating students and professionals who would like to Permanently Migrate to Australia.

We would like to advertise following services to our potential clients:

AUSTRALIA NEEDS YOU!!!

# Are you young and energetic individual?
# Do you have qualifications, work experiences or both?
# Perhaps you would like to open a small business, and sponsor yourself to live in Australia?
# Aspiring for job security and the highest living standards?

Contact us to find out how we can help you with Permanent Migration to Australia.

First consultation and eligibility assessment is free ! Tell your friends about us and receive a discount on your future fees!!

For more information please visit our website: www.pelmora-links.org.au

(for a background we would like to use Australian themes such as: sandy beaches, ect... light colours)

Target Market(s)

Students
University graduates
Trade people with qualifications
Industry professionals
Anyone who wants to migrate to Australia

Industry/Entity Type

Security

Requirements
Must have
• our logo and website
easy to see and read the txt

Catchy Background
Nice to have
• as per our requirements
(designer questions, please e-mail: info@pelmora-links.org. au)

```html
<!DOCTYPE html>
<html lang="en">
<head>
<meta charset="utf-8">
<title>Pelmora Links – Permanent Migration to Australia</title>
<link rel="stylesheet" href="https://fonts.googleapis.com/css2?family=Roboto:wght@700&family=Roboto+Condensed:ital,wght@0,700;1,700&family=Archivo:ital,wght@0,800;1,800&display=swap">
<style>
  :root {
    --cream: #fbe9c7;
    --maroon: #8c1a1c;
    --ink: #141414;
    --sage: #d6dcb9;
    --sage-line: #cbd2ad;
    --lemon: #f4eba6;
    --apricot: #f8d08b;
    --bar: #8f1418;
    --white: #ffffff;
  }
  * { margin: 0; padding: 0; box-sizing: border-box; }
  html, body { width: 849px; height: 1200px; overflow: hidden; }
  body { background: var(--cream); }
  .flyer {
    position: relative; width: 849px; height: 1200px;
    background: var(--cream); overflow: hidden;
  }
  .headline {
    position: absolute; left: 55px; top: 42px; white-space: nowrap;
    font: italic 700 55px/1 "Roboto Condensed", "Arial Narrow", sans-serif;
    color: var(--maroon); letter-spacing: 0.3px;
  }
  .criteria {
    position: absolute; left: 48px; top: 106px; list-style: none;
    font: 700 25px/1.15 "Roboto", Arial, sans-serif;
    color: var(--ink); letter-spacing: -0.2px;
  }
  .criteria li { position: relative; padding-left: 30px; margin-bottom: 8px; white-space: nowrap; }
  .criteria li::before {
    content: "★"; position: absolute; left: 0; top: 0;
    color: var(--maroon); font-size: 24px;
  }
  .criteria .wrap { display: block; padding-left: 6px; }
  .band {
    position: absolute; left: 0; width: 849px;
    display: flex; flex-direction: column; justify-content: center; align-items: center;
    text-align: center; white-space: nowrap;
    font-family: "Archivo", "Arial Black", sans-serif; font-weight: 800;
  }
  .band-offer { top: 303px; height: 102px; background: var(--sage);
    border-top: 1px solid var(--sage-line); }
  .band-offer::after { content: ""; position: absolute; left: 0; right: 0; top: 42px;
    border-top: 1px solid var(--sage-line); }
  .band-offer p { font-style: italic; font-size: 25px; line-height: 40px; color: var(--ink); letter-spacing: 1.6px; }
  .band-offer .free { color: var(--maroon); font-size: 32px; }
  .band-contact { top: 405px; height: 100px; background: var(--lemon); }
  .band-contact p { font-size: 25px; line-height: 34px; color: var(--maroon); letter-spacing: 1.7px; }
  .band-referral { top: 505px; height: 93px; background: var(--apricot); }
  .band-referral p { font-size: 25px; line-height: 32px; color: var(--ink); letter-spacing: 1.8px; }
  .band-more { top: 600px; height: 70px; }
  .band-more p { font-style: italic; font-size: 25px; line-height: 30px; color: var(--ink); letter-spacing: 3.6px; }
  .band-web { top: 670px; height: 63px; background: var(--bar); }
  .band-web p { font-family: "Archivo", "Arial Black", sans-serif; font-weight: 800;
    font-size: 35px; color: var(--white); letter-spacing: 0.6px; }
  .hero-photo {
    position: absolute; left: 192px; top: 730px; width: 448px; height: 276px;
    background: linear-gradient(160deg, #d9b58c 0%, #b98a6a 45%, #6f7f8c 75%, #c85a4a 100%);
  }
  .brand {
    position: absolute; left: 0; width: 849px; top: 1040px;
    display: flex; align-items: center; justify-content: center; gap: 22px;
  }
  .brand-square { width: 44px; height: 44px; background: var(--maroon); }
  .brand-name {
    font: 700 58px/1 "Roboto Condensed", "Arial Narrow", sans-serif;
    color: var(--maroon); letter-spacing: 0.5px;
  }
</style>
</head>
<body>
<main class="flyer">
  <h1 class="headline">AUSTRALIA NEEDS YOU if you are</h1>
  <ul class="criteria">
    <li>Young and energetic individual</li>
    <li>Is qualified and has work experiences</li>
    <li>Interested to open a small business and sponsor<span class="wrap">yourself to live in Australia</span></li>
    <li>Aspiring for job security and highest living standards</li>
  </ul>

  <section class="band band-offer">
    <p>First consultation and eligibility</p>
    <p>assessment is <span class="free">FREE</span></p>
  </section>
  <section class="band band-contact">
    <p>Contact us and find out how we can help<br>you with Permanent Migration to Australia</p>
  </section>
  <section class="band band-referral">
    <p>Tell your friends about us and get a discount<br>on your future fees!</p>
  </section>
  <section class="band band-more">
    <p>Visit our website and know more<br>about our other visa services</p>
  </section>
  <section class="band band-web">
    <p>www.pelmora-links.org.au</p>
  </section>

  <div class="hero-photo" role="img" aria-label="Photo of three smiling young people giving thumbs up"></div>

  <footer class="brand">
    <div class="brand-square" aria-hidden="true"></div>
    <div class="brand-name">Pelmora Links</div>
  </footer>
</main>
</body>
</html>
```